Landing page for buying gold and stamps

Create a landing page for our purchase. We buy postage stamps, franked goods, gold coins, scrap gold, silver money, etc. We don't want to sell anything to people, we just shop. So the visitors should send their old gold, their stamps, etc. by post. We then estimate the value and transfer the money by bank or you can collect it in cash.

The visitor should see what he can sell. If he fills in his contact details, he will receive our purchase form and the mailing label by post so that he can send in his sales goods free of charge. Or he can call us or write an e-mail and come to us directly.

We buy:
When the form is filled out, an email will be sent to our address with the following data:
Surname
First name
Street, Nr.
Post loan number
place
What do you want to sell

In the appendix I have added designs of flyers. You can see what we buy on it. What is missing on the flyer, however, are stamps, franking goods and rarities. In addition, the design should be similar. The logo can also be used.

In addition, the following text should be on the page:
Do you need help selling an inherited collection? Feel free to contact us. We are happy to help. We have been in the stamp and coin trade for nearly 100 years.

I have also attached a picture of the stamp as an attachment. This should also be put on the side with old gold and gold coins.

And here you will find our current purchase pages:
https://www.briefhaus-tanner.ch/ankauf-gold-und-silber
https://www.briefhaus-tanner.ch/ankauf-frankatur

Competitors' pages:
https://www.edelwertplatz.ch/goldankauf/
https://www.talerbruhin.ch/ankauf-1/altgold-ankauf1.html?gclid=Xq7RtLwPzN2vKdFaYbHsUmEcGjTnQoVrZiBxWkLpDyAsCfNhMuJbOeTgIlKwSvHaRdYqPzXnBmCtGuFoLiEkJrQsWvTy

Target Market(s)

Private persons

Font styles to use
Serif
Sans Serif

Requirements
Must have
• It must be clear that anyone who wants to sell their gold, stamps or coins can do so easily from home by post. You no longer have to go to a store.
Steps to Sell:
1. You fill out your contact details
2. We will send you a form and a label for shipping (no postage for you!)
3. You will receive a non-binding purchase offer
4. You will receive the money transferred or you can collect it in cash (or we will send you the valuables you have sent back)

You have no costs! Simply sell your gold or stamps from home.

```html
<!DOCTYPE html>
<html lang="en">
<head>
<meta charset="utf-8">
<title>Briefhaus Tanner – Sell Your Gold or Stamps from Home</title>
<link rel="stylesheet" href="https://fonts.googleapis.com/css2?family=Montserrat:ital,wght@0,400;0,500;0,600;0,700;1,400;1,500&display=swap">
<style>
:root{
  --ink:#1b1b1b;
  --hero-dark:#161616;
  --hero-mid:#2b2b2b;
  --gold:#f5c452;
  --gold-deep:#b98022;
  --amber:#a8690f;
  --amber-dark:#6e430b;
  --form-bg:#f8c95f;
  --brown:#8a5515;
  --cream:#f6ead2;
  --footer:#7b4b10;
  --white:#ffffff;
}
*{box-sizing:border-box;margin:0;padding:0}
html,body{width:1200px;height:3195px;overflow:hidden}
body{font-family:"Montserrat",sans-serif;color:var(--ink);background:var(--cream);position:relative}
section,footer{position:absolute;left:0;width:1200px}
.placeholder{position:absolute}

/* Hero */
.hero{top:0;height:761px;background:radial-gradient(ellipse at 50% 30%,var(--hero-mid),var(--hero-dark) 75%)}
.brand{position:absolute;display:flex;align-items:center;gap:10px;font-weight:700;color:#d9272e;font-size:24px;letter-spacing:.5px}
.brand-mark{width:18px;height:18px;border-radius:50%;background:#d9272e}
.hero .brand{left:68px;top:54px}
.hero-icons{position:absolute;left:1028px;top:44px;display:flex;gap:14px}
.hero-title{position:absolute;top:140px;width:100%;text-align:center;font-size:75px;line-height:84px;font-weight:600;
  background:linear-gradient(180deg,#f8e3a4 0%,#d6a441 55%,#8d5c13 100%);-webkit-background-clip:text;background-clip:text;color:transparent;letter-spacing:-1px}
.hero-sub{position:absolute;top:334px;width:100%;text-align:center;color:var(--white);font-size:21px;font-weight:500}
.btn{position:absolute;display:flex;align-items:center;justify-content:center;font-weight:600;font-size:17px;border-radius:3px;text-decoration:none}
.btn-sell{left:524px;top:396px;width:152px;height:47px;background:var(--gold);color:var(--ink)}
.coins{left:370px;top:462px;width:455px;height:270px;border-radius:50%;background:radial-gradient(circle,#e9c46a,#b48525 60%,rgba(40,30,10,0) 72%)}

/* Gold and silver */
.buy{top:761px;height:592px;background:radial-gradient(ellipse at 70% 35%,#c68520,var(--amber) 45%,var(--amber-dark) 100%)}
.buy h2{position:absolute;top:812px;top:51px;width:100%;text-align:center;font-size:38px;font-weight:600;color:var(--gold)}
.values{position:absolute;top:112px;width:100%;display:flex;justify-content:center;gap:14px;font-style:italic;font-size:27px;color:var(--white)}
.values span{display:flex;align-items:center;gap:6px}
.items{position:absolute;top:161px;width:100%;text-align:center;font-size:21px;color:var(--gold);font-weight:500}
.buy .brand{left:150px;top:315px;font-size:26px}
.stamp{left:515px;top:222px;width:171px;height:190px;background:linear-gradient(135deg,#8fb3c8,#c8473e 50%,#7a9fb8)}
.badge{left:864px;top:262px;width:132px;height:132px;border-radius:50%;background:radial-gradient(circle,#fff 55%,#d8a93a 58%)}
.buy-phone{position:absolute;top:456px;width:100%;display:flex;justify-content:center;align-items:center;gap:8px;font-size:32px;color:var(--white);font-weight:500}
.contact-row{position:absolute;top:514px;width:100%;display:flex;justify-content:center;gap:34px;font-size:19px;color:var(--white);font-weight:500}
.contact-row span{display:flex;align-items:center;gap:9px}

/* Form */
.order{top:1353px;height:628px;background:var(--form-bg)}
.order-intro{position:absolute;top:44px;width:100%;text-align:center;font-size:20px;line-height:29px;font-weight:500}
.field{position:absolute;width:422px;height:46px;border:1.5px solid #3b2a10;border-radius:3px;padding-left:17px;display:flex;align-items:center;font-size:15px;font-weight:500}
.col-a{left:170px}.col-b{left:608px}
.r1{top:137px}.r2{top:202px}.r3{top:266px}
.select{left:389px;top:331px;justify-content:space-between;padding-right:22px}
.btn-submit{left:524px;top:418px;width:152px;height:47px;background:var(--brown);color:var(--white)}
.order-alt{position:absolute;top:500px;width:100%;text-align:center;font-size:21px;font-weight:500}
.order-contacts{position:absolute;top:543px;width:100%;display:flex;justify-content:center;gap:40px;font-size:35px;font-weight:500}
.order-contacts span{display:flex;align-items:center;gap:10px}

/* Heritage */
.heritage{top:1981px;height:492px;background:radial-gradient(ellipse at 50% 55%,#3a2410,#0a0807 65%)}
.heritage p{position:absolute;top:60px;width:100%;text-align:center;color:var(--white);font-size:22px;line-height:30px;font-weight:500}
.century{left:475px;top:168px;width:244px;height:164px;border-radius:50%;background:radial-gradient(circle,#d99a4b,#8a5520 60%,rgba(0,0,0,0) 72%)}
.btn-contact{left:521px;top:386px;width:151px;height:47px;background:var(--brown);color:var(--white)}

/* Directions */
.directions{top:2473px;height:615px;background:var(--cream)}
.directions h2{position:absolute;top:36px;width:100%;text-align:center;font-size:37px;font-weight:500;color:var(--brown)}
.directions h2 strong{font-weight:700}
.map-overview{left:93px;top:137px;width:440px;height:372px;background:linear-gradient(160deg,#efe3c8,#e6d6b4)}
.map-site{left:570px;top:119px;width:565px;height:452px;background:linear-gradient(160deg,#ece4d4,#ddd6c6)}

.footer{top:3088px;height:107px;background:var(--footer);display:flex;align-items:center;justify-content:center;color:var(--gold);font-size:16px}
</style>
</head>
<body>

<section class="hero">
  <div class="brand"><span class="brand-mark"></span>Briefhaus Tanner</div>
  <div class="hero-icons">
    <svg width="24" height="24" viewBox="0 0 24 24" fill="none" stroke="#f5c452" stroke-width="1.8"><circle cx="12" cy="12" r="10"/><circle cx="12" cy="10" r="3.5"/><path d="M5.5 19c2-3 11-3 13 0"/></svg>
    <svg width="24" height="24" viewBox="0 0 24 24" fill="none" stroke="#f5c452" stroke-width="2"><circle cx="10" cy="10" r="7"/><path d="M15 15l6 6"/></svg>
    <svg width="24" height="24" viewBox="0 0 24 24" fill="none" stroke="#f5c452" stroke-width="1.8"><path d="M4 8h16l-1 13H5z"/><path d="M8 8a4 4 0 0 1 8 0"/></svg>
  </div>
  <h1 class="hero-title">Sell Your Gold or Stamps<br>from Home</h1>
  <p class="hero-sub">We buy postage stamps, franked goods, gold coins, scrap gold, silver money, etc.</p>
  <a class="btn btn-sell" href="#order">Sell Now</a>
  <div class="placeholder coins" role="img" aria-label="Pile of gold coins"></div>
</section>

<section class="buy">
  <h2>We look for and buy Gold and Silver</h2>
  <div class="values">
    <span><svg width="22" height="22" viewBox="0 0 24 24" fill="none" stroke="#fff" stroke-width="2"><circle cx="12" cy="12" r="9"/><path d="M8 12l3 3 6-7"/></svg>Sicher</span>
    <span><svg width="22" height="22" viewBox="0 0 24 24" fill="none" stroke="#fff" stroke-width="2"><circle cx="12" cy="12" r="9"/><path d="M8 12l3 3 6-7"/></svg>Transparenz</span>
    <span><svg width="22" height="22" viewBox="0 0 24 24" fill="none" stroke="#fff" stroke-width="2"><circle cx="12" cy="12" r="9"/><path d="M8 12l3 3 6-7"/></svg>Fair</span>
  </div>
  <p class="items">Goldvreneli | Old Gold and Silver | Coins | Bars | Medals | Watches | Rings | Chains</p>
  <div class="brand"><span class="brand-mark"></span>Briefhaus Tanner</div>
  <div class="placeholder stamp" role="img" aria-label="Historic postage stamp"></div>
  <div class="placeholder badge" role="img" aria-label="Instant cash badge"></div>
  <div class="buy-phone">
    <svg width="30" height="30" viewBox="0 0 24 24" fill="#f5c452"><path d="M6.6 10.8a15 15 0 0 0 6.6 6.6l2.2-2.2c.3-.3.7-.4 1-.2 1.1.4 2.3.6 3.6.6.6 0 1 .4 1 1V20c0 .6-.4 1-1 1A17 17 0 0 1 3 4c0-.6.4-1 1-1h3.5c.6 0 1 .4 1 1 0 1.3.2 2.5.6 3.6.1.3 0 .7-.2 1z"/></svg>
    0041 61 555 27 40
  </div>
  <div class="contact-row">
    <span><svg width="20" height="20" viewBox="0 0 24 24" fill="none" stroke="#f5c452" stroke-width="2"><circle cx="12" cy="12" r="9"/><path d="M3 12h18M12 3c3 3 3 15 0 18M12 3c-3 3-3 15 0 18"/></svg>www.briefhaus-tanner.ch</span>
    <span><svg width="20" height="20" viewBox="0 0 24 24" fill="#f5c452"><path d="M2 5h20v14H2z"/><path d="M2 5l10 8 10-8" stroke="#a8690f" stroke-width="1.6" fill="none"/></svg>info@briefhaus-tanner.ch</span>
    <span><svg width="20" height="20" viewBox="0 0 24 24" fill="#f5c452"><path d="M12 2a7 7 0 0 0-7 7c0 5 7 13 7 13s7-8 7-13a7 7 0 0 0-7-7zm0 9.5a2.5 2.5 0 1 1 0-5 2.5 2.5 0 0 1 0 5z"/></svg>Lindenweg 14, 4900 Talwil</span>
  </div>
</section>

<section class="order" id="order">
  <p class="order-intro">fills in his contact details, he will receive our purchase form and<br>the mailing label by post so that he can send in his sales goods free of charge.</p>
  <div class="field col-a r1">Surname*</div>
  <div class="field col-b r1">First Name*</div>
  <div class="field col-a r2">Phone Number*</div>
  <div class="field col-b r2">Street, Nr.*</div>
  <div class="field col-a r3">Post Loan Number.*</div>
  <div class="field col-b r3">Place*</div>
  <div class="field select">What Do You Want To Sell
    <svg width="20" height="12" viewBox="0 0 20 12" fill="none" stroke="#1b1b1b" stroke-width="2"><path d="M1 1l9 9 9-9"/></svg>
  </div>
  <a class="btn btn-submit" href="#order">Submit</a>
  <p class="order-alt">Or call us or write an e-mail and come to us directly</p>
  <div class="order-contacts">
    <span><svg width="32" height="32" viewBox="0 0 24 24" fill="#8a5515"><path d="M6.6 10.8a15 15 0 0 0 6.6 6.6l2.2-2.2c.3-.3.7-.4 1-.2 1.1.4 2.3.6 3.6.6.6 0 1 .4 1 1V20c0 .6-.4 1-1 1A17 17 0 0 1 3 4c0-.6.4-1 1-1h3.5c.6 0 1 .4 1 1 0 1.3.2 2.5.6 3.6.1.3 0 .7-.2 1z"/></svg>0041 61 555 27 40</span>
    <span><svg width="30" height="30" viewBox="0 0 24 24" fill="#8a5515"><path d="M2 5h20v14H2z"/><path d="M2 5l10 8 10-8" stroke="#f8c95f" stroke-width="1.6" fill="none"/></svg>info@briefhaus-tanner.ch</span>
  </div>
</section>

<section class="heritage">
  <p>Do you need help selling an inherited collection? Feel free to contact us.<br>We are happy to help. We have been in the stamp and coin trade for nearly</p>
  <div class="placeholder century" role="img" aria-label="100th year anniversary emblem"></div>
  <a class="btn btn-contact" href="#order">Contact Us</a>
</section>

<section class="directions">
  <h2><strong>Anfahrt</strong> - Wie Sie uns finden</h2>
  <div class="placeholder map-overview" role="img" aria-label="Regional route map to the shop"></div>
  <div class="placeholder map-site" role="img" aria-label="Site plan of the industrial area with shop location"></div>
</section>

<footer class="footer">copyright © 2020, briefhaus-tanner.ch</footer>

</body>
</html>
```